BrightLoom business card

We are a performing arts company providing training (to both kids and adults) as well as performers for events. We hope to bring joy and confidence on stage to the people we train, as well as joy to the audience when our artistes perform. Designs should convey the joy, confidence and vibrancy on stage. Design business card using the attached logo. Card to include name, mobile tel, email address, company address, and website. Double sided. To also include the following list of what the company does:
• Training & Enrichment
• Private & Corporate Entertainment
- Music composition & production

Industry/Entity Type

Training

Contact Information for Business Card

Card to include name, mobile tel, email address, company address, and website. Double sided. To also include the following list of what the company does:
• Training & Enrichment

Requirements
Nice to have
• Card need not be the traditional rectangular in shape but not too outrageous.

```html
<!DOCTYPE html>
<html lang="en">
<head>
<meta charset="utf-8">
<title>BrightLoom business card</title>
<link rel="stylesheet" href="https://fonts.googleapis.com/css2?family=Arimo:ital,wght@0,400;0,700;1,400&display=swap">
<style>
  :root {
    --page: #e7e4e0;
    --panel-deep: #141a2e;
    --panel-mid: #1d3a6b;
    --panel-glow: #2f6fb0;
    --frost: #f3f2ef;
    --frost-edge: #dcdad6;
    --divider: #8a2f5a;
    --text-light: #ffffff;
    --text-soft: #e4e8f0;
    --text-list: #c9ccd4;
    --brand: #4a2c7a;
  }
  * { margin: 0; padding: 0; box-sizing: border-box; }
  html, body { width: 1200px; height: 969px; overflow: hidden; background: var(--page); }
  .card {
    position: absolute; left: 100px; top: 201px; width: 1000px; height: 567px;
    border-radius: 22px; overflow: hidden; background: var(--frost);
    box-shadow: 0 10px 30px rgba(0,0,0,.18);
    font-family: "Arimo", Arial, sans-serif;
  }
  .card-art { position: absolute; inset: 0; }
  .contact { position: absolute; left: 44px; top: 0; color: var(--text-soft); }
  .name { position: absolute; top: 52px; font-size: 35px; font-weight: 700; color: var(--text-light); white-space: nowrap; }
  .address { position: absolute; top: 124px; font-size: 24px; line-height: 37px; white-space: nowrap; }
  .lines { position: absolute; top: 212px; list-style: none; font-size: 24px; }
  .lines li { height: 39px; display: flex; align-items: center; gap: 14px; white-space: nowrap; }
  .lines svg { width: 24px; height: 24px; fill: var(--text-soft); flex: none; }
  .services { position: absolute; top: 394px; list-style: none; font-size: 25px; font-style: italic; color: var(--text-list); }
  .services li { height: 48px; display: flex; align-items: center; white-space: nowrap; }
  .services li::before { content: ""; width: 10px; height: 10px; border-radius: 50%; background: var(--text-list); margin-right: 16px; }
  .brand { position: absolute; left: 560px; top: 300px; width: 420px; display: flex; justify-content: center; }
  .brand-name { display: inline-flex; align-items: center; gap: 14px; font-weight: 700; font-size: 56px; line-height: 1; color: var(--brand); }
  .brand-dot { width: 22px; height: 22px; border-radius: 50%; background: var(--brand); }
</style>
</head>
<body>
<div class="card">
  <svg class="card-art" viewBox="0 0 1000 567" width="1000" height="567">
    <defs>
      <radialGradient id="panelGlow" cx="0.45" cy="0.45" r="0.7">
        <stop offset="0" stop-color="var(--panel-glow)"/>
        <stop offset="0.5" stop-color="var(--panel-mid)"/>
        <stop offset="1" stop-color="var(--panel-deep)"/>
      </radialGradient>
      <radialGradient id="frostGlow" cx="0.65" cy="0.4" r="0.6">
        <stop offset="0" stop-color="#ffffff"/>
        <stop offset="1" stop-color="var(--frost-edge)"/>
      </radialGradient>
    </defs>
    <rect x="0" y="0" width="1000" height="567" fill="url(#frostGlow)"/>
    <rect role="img" aria-label="Faint music notes and dancing figures decoration" x="560" y="0" width="440" height="567" fill="#e9e3e6" opacity="0.45"/>
    <path d="M568 0 C 505 150, 500 420, 548 567 L 556 567 C 509 420, 513 150, 576 0 Z" fill="var(--divider)"/>
    <path d="M0 0 H568 C 505 150, 500 420, 548 567 H0 Z" fill="url(#panelGlow)"/>
  </svg>

  <div class="contact">
    <h1 class="name">Daniel Reyes</h1>
    <p class="address">Suite 408 Harbor Lane<br>Riverton, Zip 5127, Avalora</p>
    <ul class="lines">
      <li><svg viewBox="0 0 24 24"><path d="M3 9c0-3 4-5 9-5s9 2 9 5v2h-5V9c-1-1-7-1-8 0v2H3z"/><path d="M6 13h12l2 7H4z"/></svg>127 555 0142</li>
      <li><svg viewBox="0 0 24 24"><path d="M7 1h10a2 2 0 0 1 2 2v18a2 2 0 0 1-2 2H7a2 2 0 0 1-2-2V3a2 2 0 0 1 2-2zm0 3v14h10V4zm5 15.5a1.2 1.2 0 1 0 0 2.4 1.2 1.2 0 0 0 0-2.4z"/></svg>345 555 0198</li>
      <li><svg viewBox="0 0 24 24"><path d="M2 5h20v14H2zm2 2v.5l8 6 8-6V7zm0 3v7h16v-7l-8 6z"/></svg>hello@loomstagearts.example</li>
      <li><svg viewBox="0 0 24 24"><path d="M12 2a10 10 0 1 0 0 20 10 10 0 0 0 0-20zm0 2c1.2 1.3 2 3.2 2.3 5H9.7C10 7.2 10.8 5.3 12 4zM4.3 11h3.4a16 16 0 0 0 0 2H4.3a8 8 0 0 1 0-2zm5.4 0h4.6a14 14 0 0 1 0 2H9.7a14 14 0 0 1 0-2zm6.6 0h3.4a8 8 0 0 1 0 2h-3.4a16 16 0 0 0 0-2zM9.7 15h4.6c-.3 1.8-1.1 3.7-2.3 5-1.2-1.3-2-3.2-2.3-5z"/></svg>www.loomstagearts.example</li>
    </ul>
    <ul class="services">
      <li>Training &amp; Enrichment</li>
      <li>Private &amp; Corporate Entertainment</li>
      <li>Music composition &amp; production</li>
    </ul>
  </div>

  <div class="brand">
    <div class="brand-name"><span class="brand-dot"></span>BrightLoom</div>
  </div>
</div>
</body>
</html>
```